Home Inspection Flyer

Looking to have flyer designed that features our business, services, and our contact information. There are three of us. We are all business partners and do not have a company phone number. So each of us would need to be listed on flyer along with our individual phone number. Everything you could possibly need is on our website from logo to services and contact information. https://larkmeadowhomereview.com/. If you could possible incorporate our company colors that would be great. You can find those in our logo top left hand side of website and attached. Please also include our velcorant and brev logos ( home inspector affiliations ) on brochure as well. Those can be found on website. Please feel free to reach out with any questions.
Thanks
Dale
Updates
Looking to get a few tri fold designs. All the ones submitted have been 8x11

```html
<!DOCTYPE html>
<html lang="en">
<head>
<meta charset="UTF-8">
<title>Larkmeadow Home Review – Home Buyer Inspection Flyer</title>
<link href="https://fonts.googleapis.com/css2?family=Montserrat:wght@400;600;700;800&display=swap" rel="stylesheet">
<style>
  :root {
    --backdrop: #bcc1c8;
    --paper: #ffffff;
    --ink: #141414;
    --muted: #8a8a8a;
    --green: #7fb241;
    --band: #0c0c0c;
    --badge: #b89a3a;
    --badge-alt: #7a7a6e;
  }
  * { box-sizing: border-box; margin: 0; padding: 0; }
  html, body { width: 1200px; height: 1200px; overflow: hidden; }
  body {
    background: var(--backdrop);
    font-family: "Montserrat", sans-serif;
    color: var(--ink);
    position: relative;
  }
  .flyer {
    position: absolute;
    left: 170px; top: 44px;
    width: 860px; height: 1112px;
    background: var(--paper);
    display: flex; flex-direction: column;
    box-shadow: 0 6px 24px rgba(0,0,0,.12);
  }
  .brand {
    padding-top: 64px;
    text-align: center;
  }
  .brand-name {
    display: inline-flex; align-items: center; gap: 14px;
    font-size: 40px; font-weight: 800; letter-spacing: .5px;
    color: var(--ink);
  }
  .brand-mark { width: 22px; height: 22px; background: var(--green); }
  .brand-tagline {
    margin-top: 10px;
    font-size: 17px; color: var(--muted); letter-spacing: .5px;
  }
  .intro {
    padding: 40px 90px 0;
    text-align: center;
  }
  .intro-title { font-size: 23px; font-weight: 800; margin-bottom: 12px; }
  .intro p { font-size: 16px; line-height: 1.5; margin-bottom: 18px; }
  .services-heading {
    display: flex; align-items: center; gap: 16px;
    padding: 6px 56px 0;
    font-size: 21px; font-weight: 800;
  }
  .services-heading::before, .services-heading::after {
    content: ""; flex: 1; height: 1px; background: #777;
  }
  .services {
    display: flex; justify-content: space-between;
    padding: 22px 56px 0;
    list-style: none;
  }
  .service {
    width: 96px; text-align: center;
    font-size: 11px; font-weight: 700; line-height: 1.2;
  }
  .service svg { width: 46px; height: 46px; display: block; margin: 0 auto 8px; }
  .photos {
    margin-top: 26px;
    display: grid; grid-template-columns: repeat(3, 1fr); gap: 8px;
    height: 200px;
  }
  .photo { height: 100%; }
  .photo-sewer { background: linear-gradient(135deg, #9ea3a6, #5d6266 60%, #2a3a5c); }
  .photo-house { background: linear-gradient(180deg, #6f9fd6 0%, #c9d8e6 40%, #d9d3c8 65%, #5f8d3d 100%); }
  .photo-meter { background: linear-gradient(135deg, #3b2c22, #6a5442 55%, #c9a227 80%, #2c211a); }
  .contact {
    flex: 1;
    margin-top: 8px;
    background: var(--band);
    color: #fff;
    position: relative;
    padding: 34px 40px 0;
    text-align: center;
  }
  .contact-title { font-size: 27px; font-weight: 700; margin-bottom: 18px; white-space: nowrap; }
  .partners { list-style: none; font-size: 22px; font-weight: 700; line-height: 1.4; }
  .partner-phone { color: var(--green); }
  .badge {
    position: absolute; width: 84px; height: 84px; border-radius: 50%;
  }
  .badge-left { left: 56px; bottom: 40px; background: var(--badge); }
  .badge-right { right: 56px; top: 96px; background: var(--badge-alt); }
</style>
</head>
<body>
<main class="flyer">
  <header class="brand">
    <div class="brand-name"><span class="brand-mark"></span>LARKMEADOW HOME REVIEW</div>
    <div class="brand-tagline">Inspections | Consulting | Testing</div>
  </header>

  <section class="intro">
    <h1 class="intro-title">What is a Larkmeadow Home Buyer Inspection?</h1>
    <p>A home buyer inspection is a visual examination of a home and its systems: interior plumbing, electrical, roof, attics (temperature permitting), and visible areas of walls, ceilings, floors, foundations, etc.</p>
    <p>Our team of top-industry professional inspectors is committed to providing detailed, full-color inspection reports that cover the mechanical and structural components of a home and follow the stringent guidelines and standards of practice of the Brev Society of Home Inspectors.</p>
  </section>

  <h2 class="services-heading">Our services:</h2>
  <ul class="services">
    <li class="service">
      <svg viewBox="0 0 48 48" fill="var(--green)"><path d="M24 6 3 24h6v18h12V31h6v11h12V24h6z"/></svg>
      Home Inspection
    </li>
    <li class="service">
      <svg viewBox="0 0 48 48" fill="var(--green)"><ellipse cx="24" cy="28" rx="11" ry="14"/><circle cx="24" cy="12" r="6"/><path d="M6 20h8v3H6zm28 0h8v3h-8zM6 32h8v3H6zm28 0h8v3h-8z"/></svg>
      Pest Inspection
    </li>
    <li class="service">
      <svg viewBox="0 0 48 48" fill="none" stroke="var(--green)" stroke-width="4"><path d="M20 30V8a4 4 0 0 1 8 0v22"/><circle cx="24" cy="36" r="7" fill="var(--green)"/></svg>
      Radon Inspection
    </li>
    <li class="service">
      <svg viewBox="0 0 48 48" fill="none" stroke="var(--green)" stroke-width="4"><path d="M11 4h18l9 9v31H11z"/><rect x="17" y="22" width="10" height="10" fill="var(--green)" stroke="none"/><path d="M27 25l6-3v10l-6-3z" fill="var(--green)" stroke="none"/></svg>
      Sewer Camera Inspection
    </li>
    <li class="service">
      <svg viewBox="0 0 48 48" fill="var(--green)"><path d="M8 44V18a12 12 0 0 1 24 0h-5a7 7 0 0 0-14 0v26z"/><path d="M26 20h14l-4 6H30z"/><circle cx="32" cy="32" r="2"/><circle cx="38" cy="32" r="2"/><circle cx="35" cy="38" r="2"/></svg>
      Water Sample Test
    </li>
    <li class="service">
      <svg viewBox="0 0 48 48" fill="none" stroke="var(--green)" stroke-width="4" stroke-linecap="round"><path d="M4 12q5-5 10 0t10 0 10 0 10 0M4 24q5-5 10 0t10 0 10 0 10 0M4 36q5-5 10 0t10 0 10 0 10 0"/></svg>
      Well Flow Test
    </li>
    <li class="service">
      <svg viewBox="0 0 48 48" fill="var(--green)"><circle cx="8" cy="10" r="5"/><circle cx="20" cy="10" r="4"/><circle cx="36" cy="8" r="4"/><circle cx="8" cy="24" r="4"/><circle cx="24" cy="24" r="2"/><circle cx="40" cy="24" r="2"/><circle cx="10" cy="38" r="2"/><circle cx="28" cy="38" r="2"/><circle cx="42" cy="38" r="2"/></svg>
      Septic Dye Flow Test
    </li>
  </ul>

  <div class="photos">
    <div class="photo photo-sewer" role="img" aria-label="Sewer inspection camera monitor beside a floor drain"></div>
    <div class="photo photo-house" role="img" aria-label="House under a blue sky examined through a magnifying glass"></div>
    <div class="photo photo-meter" role="img" aria-label="Hand holding a yellow moisture meter against wooden beams"></div>
  </div>

  <footer class="contact">
    <p class="contact-title">Contact us to schedule your home inspection.</p>
    <ul class="partners">
      <li>Corbin Hale <span class="partner-phone">(555) 210-4837</span></li>
      <li>Wes Tallmadge <span class="partner-phone">(555) 382-9164</span></li>
      <li>Dale Orvik <span class="partner-phone">(555) 647-2058</span></li>
    </ul>
    <div class="badge badge-left" role="img" aria-label="Brev membership badge"></div>
    <div class="badge badge-right" role="img" aria-label="Velcorant certification badge"></div>
  </footer>
</main>
</body>
</html>
```